A live music performing company website

Hello guys!

We provide live music performance at wedding parties, business exhibitions, and dinner parties. We have three performing teams, a classic music team, a Jazz music team, and a pop music team, in the company.

We already have a logo. Now we are looking for a website proposal which should fin in with the logo and our company style. What we intend to represent is professional, elegant, and luxury atmosphere in the web design.

== Here is the spec ==

* The IA(Information Architecture) of the site will be ("Home" is the root node, "-" is the first sub-layer, "+" is the second sub-layer):

Home
- Groups(brief intro)
+Classic (detail intro)
+Jazz (detail intro)
+Pop (detail intro)
- Members
- Videos
+ Classic
+ Jazz
+ Pop
- Pricing
- Order

*One home page.

*Several internal pages:
- One is used to brief the three performing groups. ("Groups" in the IA)
++ Three pages(or tags) to introduce each groups.
- One is for introducing our primary members ("Members" in the iA)
- One is MV sharing for each performing group. ("Videos" in the IA)
- One is for introducing our pricing packages. ("Pricing" in the IA)
- One is for making order (holds a html form). ("Order" in the IA)
- One is for usual intro pages, such as "contact us", "about us", "Jobs" ...

=== Update 2011/08/29 ===
We also need a theme for our Blog, you can assume it hosts by Quillo.

The theme has to represent the same atmosphere with the main site.
======
Updates

We just add a requirement in the "overview" section. We need a theme for your blog system. We have raised our budget from to 400, and add 2 participation payment.

Thanks!!

Just uploaded a .pdf, which includes our company name and slogan. The logo has been uploaded as an .ai file yesterday.

We have added a requirement in the "Must Have Priorities", which is about the home page.

We have added a "Nice to Have Priorities", which is about a "Chatterpage Like box" element on the home page.

Please check it up. Thanks!!!

About the "Photo slider", we prefer the sixth and seventh one in this page.

http://codetrailnotes.brimwaylab.net/web-programming/47-scripting/85-30-best-photo-plugins-sliders-slideshow-galleries-and-scrollers.html

Target Market(s)

*People who are going to get married in the near future.

*People who are going to launch a dinner party.

*Business people who are going to raise an exhibition.

Industry/Entity Type

Wedding

Requirements
Must have
• *Home page:
+ An area will be used to put a photo slider to show our recent performances.
+ Must be arranged at the resolution of 960px * 600px.
+ Has to present the company name, the logo, and the slogan. How to arrange all of them is up to designer. (Company name and slogan are written in Chinese, they are saved in the pdf as an attachment file.)

*Internal pages:
+ The width of internal pages has to be 960px.

* "Videos" page:
+ Has the capability to arrange the videos by:
- Date (Default arrangement)
- Geo location (With a Wandero map, once our customers click on the pin, the web page could show a list of recording at the location.)
- Category (Biz exhibitions, wedding parties, or dinner parties)
Nice to have
• * Designers can use the preview photos(with watermark) on Pixvaultery.com. We can go to purchase the legal usage once your design has been accepted.

* If it's possible to embed a "Chatterpage Like box" (Please reference it at: http://developers.chatterpage.net/docs/reference/plugins/like-box/) on the home page, it will be great. But if the box might threat the integrity of the page, then don't use it.
Should not have
• * No Flash.
* No tech coding.

```html
<!DOCTYPE html>
<html lang="zh-Hant">
<head>
<meta charset="utf-8">
<title>和弦藝術 — 用音樂愉悅您的賓客</title>
<link rel="stylesheet" href="https://fonts.googleapis.com/css2?family=Crimson+Text&family=Noto+Sans+TC:wght@300;400&family=Old+Standard+TT&family=Arimo:wght@400;700&display=swap">
<style>
:root{
  --header-dark:#4f6b7e;
  --header-light:#a9b9c4;
  --page:#ffffff;
  --text-grey:#8a8a8a;
  --heading-grey:#6d6d6d;
  --accent-red:#b31a17;
  --badge-dark:#7e0f0d;
  --footer:#8ea2b0;
  --box-border:#b7c0c8;
  --social-blue:#3b5998;
  --social-text:#333;
  --social-muted:#777;
  --sign-green:#5aa345;
}
*{margin:0;padding:0;box-sizing:border-box}
html,body{width:1200px;height:752px;overflow:hidden;background:var(--page)}
body{position:relative;font-family:"Old Standard TT",serif;color:var(--text-grey)}
.abs{position:absolute}

/* header */
.site-header{position:absolute;left:0;top:0;width:1200px;height:100px;
  background:linear-gradient(180deg,#6e8798 0,#6e8798 12px,#8da1ae 13px,var(--header-dark) 100%)}
.brand{position:absolute;left:37px;top:22px;width:291px;height:80px;background:#fff;
  border-radius:12px 12px 0 0;box-shadow:0 0 6px rgba(0,0,0,.25);display:flex;align-items:center;padding-left:16px;gap:16px}
.brand-dot{width:46px;height:46px;border-radius:50%;background:var(--accent-red)}
.brand-name{font-family:"Noto Sans TC",sans-serif;font-weight:400;font-size:38px;color:#555;letter-spacing:2px}
.main-nav{position:absolute;top:62px;left:0;width:1200px;height:28px}
.main-nav a{position:absolute;font-family:"Crimson Text",serif;font-size:20px;color:#eef2f5;text-decoration:none}

/* intro */
.intro-title{left:37px;top:114px;font-family:"Noto Sans TC",sans-serif;font-weight:300;font-size:34px;color:var(--heading-grey);letter-spacing:1px}
.intro-text{left:37px;top:158px;width:470px;font-size:13px;line-height:16.3px;text-align:justify;letter-spacing:.6px;color:#999}
.hero-frame{left:520px;top:117px;width:336px;height:266px;border-radius:14px;background:#f3f3f3;box-shadow:0 0 5px rgba(0,0,0,.2)}
.hero-photo{left:531px;top:129px;width:315px;height:247px;background:linear-gradient(135deg,#3d2416 0%,#8a3b1c 40%,#b51c1c 60%,#e9e4dc 100%)}
.intro-band{left:0;top:378px;width:870px;height:8px;background:linear-gradient(180deg,#e8e8e8,#fff)}

/* news and events */
.badge{width:64px;height:64px;border-radius:50%;background:radial-gradient(circle at 40% 35%,#d9301f,var(--badge-dark));
  box-shadow:0 1px 3px rgba(0,0,0,.4);color:#fff;font-family:"Crimson Text",serif;font-size:15px;line-height:15px;text-align:center;padding-top:16px}
.divider{height:6px;border-radius:50%;background:radial-gradient(ellipse at center,#dcdcdc,rgba(255,255,255,0) 70%)}
.post{width:310px}
.post-date{font-size:15px;color:#888;letter-spacing:.5px}
.post-title{margin-top:4px;font-size:18px;font-weight:400;color:#888;letter-spacing:2px}
.post-text{margin-top:3px;font-size:14px;line-height:15.5px;letter-spacing:1.1px;color:#999}
.learn-more{font-family:"Crimson Text",serif;font-size:16px;color:var(--accent-red);text-decoration:none}

/* like box */
.like-box{left:879px;top:121px;width:305px;height:601px;border:1px solid var(--box-border);background:#fff;font-family:Arimo,sans-serif}
.like-head{height:31px;background:#eceff2;border-bottom:1px solid #cfd6dc;font-size:13px;font-weight:700;color:var(--social-text);padding:8px 10px}
.sign-btn{left:12px;top:42px;width:61px;height:29px;background:var(--sign-green);border:1px solid #3f7a30;color:#fff;font-weight:700;font-size:13px;text-align:center;line-height:27px}
.small{font-size:11px;line-height:14px;color:var(--social-muted)}
.small b{color:var(--social-blue);font-weight:400}
.rule{left:8px;width:287px;height:1px;background:#dde2e6}
.page-mark{width:41px;height:41px;background:var(--social-blue)}
.page-name{font-size:14px;font-weight:700;color:var(--social-blue);white-space:nowrap}
.like-btn{width:30px;height:20px;border:1px solid #b8c1cf;background:#eef0f5;font-size:10px;color:#333;text-align:center;line-height:18px}
.feed{left:0;top:151px;width:282px;height:253px;overflow:hidden}
.scrollbar{left:284px;top:151px;width:14px;height:253px;background:#eee;border:1px solid #ccc}
.thumb{left:71px;top:60px;width:92px;height:52px;background:linear-gradient(#e6ebf3,#c9d3e3);border:1px solid #aab}
.post-link{left:174px;top:30px;width:64px;font-size:11.5px;line-height:14px;font-weight:700;color:var(--social-blue)}
.post-body{left:174px;top:110px;width:64px;font-size:10.5px;line-height:14.3px;color:#555}
.fans-count{left:10px;top:410px;font-size:11px;color:#333}
.fans-count b{color:#333}
.fans{left:10px;top:427px;width:290px;display:grid;grid-template-columns:repeat(5,52px);column-gap:5px;row-gap:6px}
.fan-photo{width:52px;height:52px}
.fan-name{font-size:9px;color:#555;text-align:center;height:14px;line-height:14px;white-space:nowrap;overflow:hidden}
.plugin-foot{left:10px;top:576px;font-size:9px;color:#555;display:flex;align-items:center;gap:5px}
.plugin-foot i{display:block;width:12px;height:12px;background:var(--social-blue)}

/* footer */
.site-footer{position:absolute;left:0;top:729px;width:1200px;height:23px;background:var(--footer);font-family:Arimo,sans-serif;font-size:10px;color:#eef2f5}
.site-footer .copy{position:absolute;left:44px;top:6px}
.site-footer nav{position:absolute;right:16px;top:4px;display:flex}
.site-footer nav a{color:#eef2f5;text-decoration:none;padding:1px 6px;border-left:1px solid #e5ebef}
.site-footer nav a:first-child{border-left:0}
</style>
</head>
<body>

<header class="site-header">
  <div class="brand"><span class="brand-dot"></span><span class="brand-name">和弦藝術</span></div>
  <nav class="main-nav">
    <a href="#" style="left:531px">Groups</a>
    <a href="#" style="left:676px">Members</a>
    <a href="#" style="left:842px">Videos</a>
    <a href="#" style="left:986px">Pricing</a>
    <a href="#" style="left:1131px">Order</a>
  </nav>
</header>

<main>
  <h1 class="abs intro-title">用音樂愉悅您的賓客</h1>
  <p class="abs intro-text">Quisque vitae pede. Nam et augue. Sed a elit. Ut vel massa. Suspendisse nibh pede, ultrices vitae, ultrices nec, mollis non nibh. Quisque vitae pede Nam et augue. Sed a elit Ut vel massa. Suspendisse nibh pede, ultrices vitae,ultrices nec, mollis non nibh. Quisque vitae pede. Nam et augue. Sed a elit. Ut vel massa. Suspendisse nibh pede, ultrices vitae ultrices nec, mollis non nibh.Quisque vitae pede Nam et augue. Sed a elit. Ut vel massa Suspendisse nibh pede ultrices vitae ultrices nec, mollis non nibh... Quisque vitae pede. Nam et augue. Sed a elit. Ut vel massa. Suspendisse nibh pede, ultrices vitae ultrices nec, mollis non nibh... Suspendisse nibh pede, ultrices vitae ultrices nec, mollis non nibh... Suspendisse nibh pede, ultrices vitae ultrices nec, mollis non nibh.Quisque vitae pede. Nam et augue.Sed a elit. Ut vel massa. Suspendisse nibh pede, ultrices vitae ultrices nec, mollis non nibh... Quisque vitae pede. Nam et augue. Sed a elit. Ut vel massa.</p>

  <div class="abs hero-frame"></div>
  <div class="abs hero-photo" role="img" aria-label="Photo slider: violin with a red rose on sheet music"></div>
  <div class="abs intro-band"></div>

  <section aria-label="Last news">
    <div class="abs badge" style="left:15px;top:396px">Last<br>News</div>
    <div class="abs divider" style="left:96px;top:410px;width:230px"></div>
    <article class="abs post" style="left:96px;top:429px">
      <div class="post-date">12.06.2011</div>
      <h2 class="post-title">Quisque vitae pede.</h2>
      <p class="post-text">Quisque vitae pede. Nam et augue. Sed a elit. Ut vel massa. Suspendisse nibh pede, ultrices vitae,ultrices nec, mollis non nibh...</p>
    </article>
    <a class="abs learn-more" href="#" style="left:299px;top:540px">Learn more...</a>
    <article class="abs post" style="left:90px;top:566px">
      <div class="post-date">12.06.2011</div>
      <h2 class="post-title" style="margin-left:6px">Quisque vitae pede.</h2>
      <p class="post-text" style="margin-left:6px">Quisque vitae pede. Nam et augue. Sed a elit. Ut vel massa. Suspendisse nibh pede, ultrices vitae,ultrices nec, mollis non nibh...</p>
    </article>
    <a class="abs learn-more" href="#" style="left:296px;top:678px">Learn more...</a>
    <div class="abs divider" style="left:130px;top:718px;width:170px"></div>
  </section>

  <section aria-label="Last events">
    <div class="abs badge" style="left:436px;top:396px">Last<br>Events</div>
    <div class="abs divider" style="left:535px;top:410px;width:230px"></div>
    <article class="abs post" style="left:535px;top:429px">
      <div class="post-date">12.06.2011</div>
      <h2 class="post-title">Quisque vitae pede.</h2>
      <p class="post-text">Quisque vitae pede. Nam et augue. Sed a elit. Ut vel massa. Suspendisse nibh pede, ultrices vitae,ultrices nec, mollis non nibh...</p>
    </article>
    <a class="abs learn-more" href="#" style="left:752px;top:540px">Learn more...</a>
    <article class="abs post" style="left:535px;top:566px">
      <div class="post-date">12.06.2011</div>
      <h2 class="post-title">Quisque vitae pede.</h2>
      <p class="post-text">Quisque vitae pede. Nam et augue. Sed a elit. Ut vel massa. Suspendisse nibh pede, ultrices vitae,ultrices nec, mollis non nibh...</p>
    </article>
    <a class="abs learn-more" href="#" style="left:762px;top:678px">Learn more...</a>
    <div class="abs divider" style="left:580px;top:718px;width:170px"></div>
  </section>

  <aside class="abs like-box" aria-label="Chatterpage Like box">
    <div class="like-head">Find us on Chatterpage</div>
    <div class="abs sign-btn">Sign Up</div>
    <p class="abs small" style="left:82px;top:43px;width:210px">Create an account or <b>log in</b> to see what your friends like.</p>
    <div class="abs rule" style="top:84px"></div>
    <div class="abs page-mark" style="left:10px;top:94px"></div>
    <div class="abs page-name" style="left:60px;top:96px">Chatterpage Platform</div>
    <div class="abs like-btn" style="left:61px;top:117px">Like</div>
    <div class="abs rule" style="top:147px"></div>

    <div class="abs feed">
      <div class="abs page-mark" style="left:10px;top:7px"></div>
      <div class="abs page-name" style="left:71px;top:10px;font-size:10.5px">Chatterpage Platform</div>
      <div class="abs thumb" role="img" aria-label="Screenshot preview of the post"></div>
      <div class="abs post-link">Platform Updates: Operation Developer Love</div>
      <div class="abs post-body">This week, we announced our Platform stability initiatives including a 90-day breaking change policy</div>
    </div>
    <div class="abs scrollbar"></div>

    <p class="abs fans-count">2,723,312 people like <b>Chatterpage Platform</b>.</p>
    <div class="abs fans">
      <div><div class="fan-photo" role="img" aria-label="Fan profile photo" style="background:#8a6a3a"></div><div class="fan-name">Arlo</div></div>
      <div><div class="fan-photo" role="img" aria-label="Fan profile photo" style="background:#3b4f7a"></div><div class="fan-name">Fenna</div></div>
      <div><div class="fan-photo" role="img" aria-label="Fan profile photo" style="background:#c9a98a"></div><div class="fan-name">Kalima</div></div>
      <div><div class="fan-photo" role="img" aria-label="Fan profile photo" style="background:#6b5a50"></div><div class="fan-name">Emil</div></div>
      <div><div class="fan-photo" role="img" aria-label="Fan profile photo" style="background:#6a3f8a"></div><div class="fan-name">Ardenio's</div></div>
      <div><div class="fan-photo" role="img" aria-label="Fan profile photo" style="background:#5c6d7a"></div><div class="fan-name">Jorah</div></div>
      <div><div class="fan-photo" role="img" aria-label="Fan profile photo" style="background:#c48a2c"></div><div class="fan-name">Guilermo</div></div>
      <div><div class="fan-photo" role="img" aria-label="Fan profile photo" style="background:#7f6e5a"></div><div class="fan-name">Galen</div></div>
      <div><div class="fan-photo" role="img" aria-label="Default profile placeholder" style="background:#c9d3e4"></div><div class="fan-name">Juno</div></div>
      <div><div class="fan-photo" role="img" aria-label="Default profile placeholder" style="background:#c9d3e4"></div><div class="fan-name">Leandrin</div></div>
    </div>
    <div class="abs plugin-foot"><i></i>Chatterpage social plugin</div>
  </aside>
</main>

<footer class="site-footer">
  <span class="copy">Copyright ©2011 All rights reserved</span>
  <nav><a href="#">Contact us</a><a href="#">Terms and Conditions</a><a href="#">Site map</a></nav>
</footer>

</body>
</html>
```